Business Card for a Mortgage Agent (myself)

I need a business card for my new job as Mortgage Agent. The Broker's logo is to be on the card as well as the brokerage License number. Not sure if to include a photo or not. Info to be on card.
Dante Roux
Mortgage Agent
Lic # M47105386
Cell: 905-614-2753
Email: danterouxk.ma@fennmail.com
Web: www.karlvostermortgages.com
TPW Brokerage Lic. # 73918

```html
<!DOCTYPE html>
<html lang="en">
<head>
<meta charset="utf-8">
<title>TPW Mortgage Agent Business Card</title>
<link href="https://fonts.googleapis.com/css2?family=Mulish:wght@400;600;700;800&display=swap" rel="stylesheet">
<style>
  :root {
    --brand-blue: #144a8c;
    --brand-yellow: #f5c518;
    --card-white: #f0eff4;
    --text-grey: #555a62;
    --rule-grey: #c9c9cf;
    --backdrop: #b7b7b7;
    --on-blue: #ffffff;
  }
  * { margin: 0; padding: 0; box-sizing: border-box; }
  html, body {
    width: 1200px; height: 900px; overflow: hidden;
    background: var(--backdrop);
    font-family: "Mulish", sans-serif;
  }
  .canvas { position: relative; width: 1200px; height: 900px; }
  .card {
    position: absolute; left: 363px; width: 475px; height: 271px; overflow: hidden;
  }
  .card--front { top: 145px; background: var(--brand-blue); }
  .card--back { top: 484px; background: var(--card-white); }

  .brand { position: absolute; display: flex; flex-direction: column; align-items: center; }
  .brand__row { display: flex; align-items: center; gap: 10px; }
  .brand__square { width: 22px; height: 22px; background: var(--brand-yellow); }
  .brand__name { font-weight: 800; letter-spacing: 1px; white-space: nowrap; }
  .brand__licence { align-self: flex-end; font-size: 8px; font-weight: 700; margin-top: 6px; }

  .card--front .brand { left: 0; right: 0; top: 92px; }
  .card--front .brand__name { color: var(--on-blue); font-size: 24px; }
  .card--front .brand__licence { color: var(--on-blue); margin-right: 110px; }
  .front-web {
    position: absolute; left: 0; right: 0; top: 232px; text-align: center;
    font-size: 11px; color: var(--on-blue);
  }
  .front-web strong { color: var(--brand-yellow); font-weight: 700; }

  .card--back .brand { left: 40px; width: 200px; top: 112px; }
  .card--back .brand__name { color: var(--brand-blue); font-size: 19px; }
  .card--back .brand__licence { color: var(--brand-blue); }

  .agent { position: absolute; left: 256px; top: 68px; right: 0; }
  .agent__name { font-size: 17px; font-weight: 800; color: var(--brand-blue); line-height: 1.1; }
  .agent__title { font-size: 11px; color: var(--text-grey); margin-top: 1px; }
  .agent__rule { height: 1px; background: var(--rule-grey); margin-top: 10px; }
  .agent__licences { margin-top: 11px; font-size: 11px; color: var(--text-grey); line-height: 14px; }
  .contact { list-style: none; margin-top: 8px; font-size: 11px; color: var(--text-grey); }
  .contact li { display: flex; align-items: center; gap: 8px; height: 14px; }
  .contact svg { width: 9px; height: 9px; fill: none; stroke: var(--brand-blue); stroke-width: 1.4; flex: none; }

  .footer-band { position: absolute; left: 0; right: 0; top: 245px; height: 15px; background: var(--brand-blue); }
  .footer-band__accent { position: absolute; right: 0; top: 0; width: 40px; height: 15px; background: var(--brand-yellow); }
</style>
</head>
<body>
<main class="canvas">
  <section class="card card--front" aria-label="Card front">
    <div class="brand">
      <div class="brand__row">
        <span class="brand__square"></span>
        <span class="brand__name">TPW True Path Wealth</span>
      </div>
      <span class="brand__licence">License #73918</span>
    </div>
    <p class="front-web">www.<strong>karlvostermortgages</strong>.com</p>
  </section>

  <section class="card card--back" aria-label="Card back">
    <div class="brand">
      <div class="brand__row">
        <span class="brand__name">TPW True Path Wealth</span>
      </div>
      <span class="brand__licence">License #73918</span>
    </div>

    <div class="agent">
      <h1 class="agent__name">Dante Roux</h1>
      <p class="agent__title">Mortgage Agent</p>
      <div class="agent__rule"></div>
      <p class="agent__licences">Lic # M47105386<br>TPW Brokerage Lic. # 73918</p>
      <ul class="contact">
        <li><svg viewBox="0 0 10 10"><rect x="2.5" y="0.8" width="5" height="8.4" rx="0.8"/></svg>905-614-2753</li>
        <li><svg viewBox="0 0 10 10"><rect x="0.7" y="2" width="8.6" height="6"/><path d="M0.7 2 L5 5.5 L9.3 2"/></svg>danterouxk.ma@fennmail.com</li>
        <li><svg viewBox="0 0 10 10"><circle cx="5" cy="5" r="4.2"/><ellipse cx="5" cy="5" rx="1.8" ry="4.2"/><path d="M0.8 5 H9.2"/></svg>www.karlvostermortgages.com</li>
      </ul>
    </div>

    <div class="footer-band"><span class="footer-band__accent"></span></div>
  </section>
</main>
</body>
</html>
```